Copper Lane Assembly Lanterns EP Design Cover

I need a CD cover design for my EP titled "Lanterns". The theme can be either the alphabetic letters, or written letters, whichever seems best for your graphic concept.<br/><br/>Please take a listen to the tracks on tunebasin here:<br/>https://tunebasin.example/copper-lane-assembly<br/>And here:<br/>https://tunebasin.example/copper-lane-assembly/silver-morning/s-KQ7rT<br/>https://tunebasin.example/copper-lane-assembly/rain-on-the-porch-demo-mix/s-WM4PZ<br/><br/>I look forward to seeing you designs and choosing one for the EP cover.

Target Market(s)

Indie-pop/rock

Colors

Designer to choose colors to be used in the design.

Requirements
Must have
• Copper Lane Assembly Logo
• Should meet Friendloop criteria for % text to picture ratio

```html
<!DOCTYPE html>
<html lang="en">
<head>
<meta charset="utf-8">
<title>Copper Lane Assembly – Lanterns EP Cover</title>
<link rel="stylesheet" href="https://fonts.googleapis.com/css2?family=Antonio:wght@400&family=Jost:wght@300&display=swap">
<style>
  :root {
    --pattern-grey: #8c8c8c;
    --pattern-grey-light: #b4b4b4;
    --wedge-black: #000000;
    --brand-red: #d90000;
    --logo-red: #dc0d0d;
    --pattern-red: #dd1717;
    --pattern-red-light: #ef6a6a;
    --ink-white: #ffffff;
  }
  * { margin: 0; padding: 0; box-sizing: border-box; }
  html, body { width: 1200px; height: 1200px; overflow: hidden; background: var(--wedge-black); }
  .cover { position: relative; width: 1200px; height: 1200px; overflow: hidden; }
  .letter-field { position: absolute; left: 0; top: 0; width: 828px; height: 1200px; }
  .brand-column { position: absolute; left: 828px; top: 0; width: 372px; height: 868px; background: var(--brand-red); }
  .logo-block {
    position: absolute; left: 18px; top: 128px; width: 336px; height: 572px;
    background: var(--logo-red);
  }
  .logo-line {
    position: absolute; left: 26px; width: 288px;
    display: flex; justify-content: center; align-items: center;
    font-family: "Antonio", "Arial Narrow", sans-serif;
    font-weight: 400; color: var(--ink-white); line-height: 1; text-transform: uppercase;
    white-space: nowrap; transform-origin: center top;
  }
  .logo-line--copper { top: 8px; font-size: 106px; letter-spacing: 0.04em; transform: scaleY(1.9); }
  .logo-line--lane { top: 234px; font-size: 106px; letter-spacing: 0.37em; text-indent: 0.37em; transform: scaleY(1.75); }
  .logo-line--assembly { top: 436px; font-size: 80px; letter-spacing: 0.02em; transform: scaleY(1.55); }
  .red-pattern {
    position: absolute; left: 828px; top: 868px; width: 372px; height: 332px;
    background: linear-gradient(160deg, var(--pattern-red) 0%, var(--pattern-red-light) 55%, var(--pattern-red) 100%);
  }
  .ep-title {
    position: absolute; left: 134px; top: 1070px;
    font-family: "Jost", "Helvetica Neue", sans-serif; font-weight: 300;
    font-size: 80px; line-height: 1; letter-spacing: 0.42em;
    color: var(--ink-white); text-transform: uppercase; white-space: nowrap;
  }
</style>
</head>
<body>
<main class="cover">
  <svg class="letter-field" width="828" height="1200" viewBox="0 0 828 1200">
    <defs>
      <linearGradient id="alphabet-tone" x1="0" y1="0" x2="1" y2="1">
        <stop offset="0" stop-color="var(--pattern-grey)"/>
        <stop offset="0.45" stop-color="var(--pattern-grey-light)"/>
        <stop offset="1" stop-color="var(--pattern-grey)"/>
      </linearGradient>
    </defs>
    <rect class="letter-field__pattern" x="0" y="0" width="828" height="868" fill="url(#alphabet-tone)" role="img" aria-label="Hand-lettered alphabet pattern in pale grey on mid grey"/>
    <polygon class="letter-field__wedge" points="0,644 828,866 828,1200 0,1200" fill="var(--wedge-black)"/>
  </svg>

  <section class="brand-column">
    <div class="logo-block">
      <span class="logo-line logo-line--copper">Copper</span>
      <span class="logo-line logo-line--lane">Lane</span>
      <span class="logo-line logo-line--assembly">Assembly</span>
    </div>
  </section>

  <div class="red-pattern" role="img" aria-label="Hand-lettered alphabet pattern in light red on red"></div>

  <h1 class="ep-title">Lanterns</h1>
</main>
</body>
</html>
```